Velvet Harbor (A luxury Travel Website)

website text attached in document below

images also attached

feel free to use other images if needed

Target Market(s)

Luxury Seekers and wealthy couples / families

Industry/Entity Type

Luxury Travel

Coding

Coded - Design and coding required

Number of Pages Required

1 page

Requirements
Must have
• A luxury design and easy use.
Nice to have
• Ease of use of page, incorporation of images into the flow of the site

```html
<!DOCTYPE html>
<html lang="en">
<head>
<meta charset="utf-8">
<title>Velvet Harbor — Luxury Travel</title>
<link rel="stylesheet" href="https://fonts.googleapis.com/css2?family=Poppins:wght@400;500;600&family=Roboto:wght@400&display=swap">
<style>
  :root {
    --brand-blue: #1565b0;
    --brand-blue-deep: #0d5aa6;
    --logo-blue: #4f86c2;
    --ink: #1f1f1f;
    --white: #ffffff;
    --muted: #666a70;
    --field-text: #2a64a8;
  }
  * { box-sizing: border-box; margin: 0; padding: 0; }
  html, body { width: 686px; height: 1200px; overflow: hidden; background: var(--white); }
  body { font-family: "Poppins", sans-serif; color: var(--ink); }
  .page { position: relative; width: 686px; height: 1200px; overflow: hidden; }

  .site-header { position: absolute; top: 0; left: 0; width: 686px; height: 42px; display: flex; align-items: center; justify-content: center; }
  .brand-name { font-family: "Poppins", sans-serif; font-weight: 400; color: var(--logo-blue); font-size: 17px; letter-spacing: 2px; }

  .hero { position: absolute; top: 42px; left: 0; width: 686px; height: 339px; }
  .hero-photo { position: absolute; inset: 0;
    background: linear-gradient(180deg, #3f73b4 0%, #2d4f78 30%, #27402f 55%, #7a5a34 70%, #1e5fa8 85%, #21406a 100%); }
  .hero-copy { position: absolute; top: 50px; left: 0; width: 686px; text-align: center; color: var(--white); }
  .hero-title { font-weight: 600; font-size: 21.5px; line-height: 28px; }
  .hero-lead { margin-top: 9px; font-size: 9.6px; line-height: 16px; font-weight: 400; }
  .slider-dots { position: absolute; right: 15px; top: 172px; display: flex; flex-direction: column; gap: 4px; }
  .slider-dots span { width: 7px; height: 7px; border-radius: 50%; background: var(--white); }
  .slider-dots span.is-dim { background: #b9c2cc; }

  .partners { position: absolute; top: 381px; left: 0; width: 686px; height: 455px; }
  .section-title { text-align: center; font-weight: 500; font-size: 14.3px; line-height: 23.5px; color: var(--ink); }
  .partners .section-title { margin-top: 41px; }
  .rule { position: absolute; height: 1.5px; width: 74px; background: var(--brand-blue); }
  .partners .rule { left: 309px; top: 90px; }
  .feature-circle { position: absolute; width: 246px; height: 246px; border-radius: 50%; border: 1px solid var(--brand-blue); top: 106px; }
  .feature-circle .photo { position: absolute; inset: 5px; border-radius: 50%; }
  .feature-hotel { left: 91px; }
  .feature-hotel .photo { background: radial-gradient(circle at 50% 45%, #6f8a6c 0%, #a9b6a3 35%, #e9e8ee 65%, #c9c1c4 100%); }
  .feature-flight { left: 355px; }
  .feature-flight .photo { background: linear-gradient(180deg, #b79c96 0%, #8c6a66 45%, #5a2a32 75%, #3e1a22 100%); }
  .btn-solid { position: absolute; left: 279px; top: 380px; width: 120px; height: 32px; border-radius: 16px; background: var(--brand-blue); color: var(--white); font-size: 10.6px; font-weight: 500; display: flex; align-items: center; justify-content: center; }

  .enquiry { position: absolute; top: 836px; left: 0; width: 686px; height: 306px; }
  .enquiry-photo { position: absolute; inset: 0; background: linear-gradient(160deg, #1468b6 0%, #155fa8 45%, #1a5a9e 70%, #1566b2 100%); }
  .enquiry .section-title { position: absolute; top: 40px; width: 686px; color: var(--white); font-size: 14.6px; }
  .enquiry .rule { left: 306px; top: 70px; background: var(--white); }
  .field { position: absolute; background: var(--white); border-radius: 2px; font-size: 7.6px; font-weight: 500; color: var(--field-text); padding: 0 10px; display: flex; align-items: center; }
  .field-sm { width: 175px; height: 27px; }
  .field-first { left: 162px; top: 86px; }
  .field-last { left: 348px; top: 86px; }
  .field-email { left: 162px; top: 120px; }
  .field-phone { left: 348px; top: 120px; }
  .field-message { left: 162px; top: 154px; width: 361px; height: 71px; align-items: flex-start; padding-top: 11px; }
  .btn-outline { position: absolute; left: 292px; top: 237px; width: 103px; height: 28px; border: 1px solid var(--white); border-radius: 14px; color: var(--white); font-size: 10.6px; font-weight: 500; display: flex; align-items: center; justify-content: center; }

  .site-footer { position: absolute; top: 1142px; left: 0; width: 686px; height: 58px; }
  .site-footer .brand-name { position: absolute; left: 78px; top: 16px; font-size: 16px; }
  .copyright { position: absolute; right: 75px; top: 21px; font-family: "Roboto", sans-serif; font-size: 7.4px; color: var(--muted); }
</style>
</head>
<body>
<div class="page">
  <header class="site-header">
    <span class="brand-name">VELVET HARBOR</span>
  </header>

  <section class="hero">
    <div class="hero-photo" role="img" aria-label="Tropical resort at dusk with palm trees, lit pavilions and an infinity pool"></div>
    <div class="hero-copy">
      <h1 class="hero-title">LOOKING TO STAY AT A 5 STAR HOTEL OR TO<br>FLY BUSINESS CLASS ANYWHERE?</h1>
      <p class="hero-lead">Share a screenshot of your travel plans and we beat<br>the price, within 24 hours.</p>
    </div>
    <div class="slider-dots"><span></span><span class="is-dim"></span><span></span></div>
  </section>

  <section class="partners">
    <h2 class="section-title">WE WORK DIRECTLY WITH HOTELS AND AIRLINES<br>TO GET YOU THE BEST PRICE,ALWAYS</h2>
    <div class="rule"></div>
    <div class="feature-circle feature-hotel"><div class="photo" role="img" aria-label="Bright hotel bedroom with white bed and leafy wall art"></div></div>
    <div class="feature-circle feature-flight"><div class="photo" role="img" aria-label="Business class seat with a traveller relaxing by the window"></div></div>
    <div class="btn-solid">BOOK NOW</div>
  </section>

  <section class="enquiry">
    <div class="enquiry-photo" role="img" aria-label="Aerial view of overwater villas in a blue lagoon"></div>
    <h2 class="section-title">TELL US ABOUT YOUR NEXT HOLIDAY PLANS</h2>
    <div class="rule"></div>
    <div class="field field-sm field-first">First Name*</div>
    <div class="field field-sm field-last">Last Name*</div>
    <div class="field field-sm field-email">Email address*</div>
    <div class="field field-sm field-phone">Phone*</div>
    <div class="field field-message">Your message</div>
    <div class="btn-outline">BOOK NOW</div>
  </section>

  <footer class="site-footer">
    <span class="brand-name">VELVET HARBOR</span>
    <p class="copyright">© 2022 VELVET HARBOR ALL RIGHT RESERVED</p>
  </footer>
</div>
</body>
</html>
```